Postcard Design

New property management company. We manage vacation rental properties on a gulf coast island. This post card will be designed to attract home owners to sign on with us to manage their property (s). We want to convay the message that we will take care if everything needed to maintain value in their investment property to attracting the right sort of renters as well as take care of accounting. We can do this because of our sister relationship with a local contractor and the fact that we are a small company planning to stay that way.
We would like to have a call to action offer of "reduced rates for new clients this month". Please fill free to play with those words. Make is snassy!
Updates

We have some good submissions. I am not sure we have found the "one" yet. We would like some work done with our "reduced rates" phrase. Try different words. It needs to be the most notices sentence. With our phone number being the second line that pops out. Please don't use paragraphs from out website. Phrases are fine. Thank you for your hard work. We look forward to seeing more designs.

Thank you all for your submissions. I appreciate your time.

Target Market(s)

Investment Property Owners from all over Texas, California, Colorado and most Southern States. Usually med to upper income and 35 +

Industry/Entity Type

Property Management

Requirements
Must have
• Catch line " relax- we'll take care of it"
Offer

Our Logo and information

Front and back small post card with return address in left corner and room for mailing label.
Nice to have
• Eye catching!

Noticeable offer

```html
<!DOCTYPE html>
<html lang="en">
<head>
<meta charset="utf-8">
<title>Sandpiper Rentals and Management Company – Postcard</title>
<link rel="stylesheet" href="https://fonts.googleapis.com/css2?family=Open+Sans:ital,wght@0,400;0,600;0,700;1,400&display=swap">
<style>
  :root {
    --navy: #202a6b;
    --sunset: #e8452c;
    --ink: #2a2a2a;
    --paper: #ffffff;
    --panel: #111111;
    --rule: #c9c9c9;
    --stage: #e4e4e4;
    --sky: #7cc4ea;
    --ocean: #4f86c6;
    --coral: #e86a6a;
  }
  * { box-sizing: border-box; margin: 0; padding: 0; }
  html, body { width: 1200px; height: 900px; overflow: hidden; }
  body {
    background: var(--stage);
    font-family: "Open Sans", Arial, sans-serif;
    color: var(--ink);
    display: flex;
    flex-direction: column;
    align-items: center;
    justify-content: center;
    gap: 22px;
  }
  .postcard {
    position: relative;
    width: 640px;
    height: 418px;
    background: var(--paper);
    box-shadow: 0 4px 14px rgba(0,0,0,.18);
    overflow: hidden;
  }

  /* ---------- front ---------- */
  .front__top-band {
    position: absolute; inset: 0 0 auto 0; height: 58px;
    background: var(--navy);
  }
  .front__web {
    position: absolute; top: 12px; right: 22px;
    color: var(--paper); font-size: 11px; font-weight: 600;
  }
  .front__wave { position: absolute; left: 0; bottom: 0; width: 640px; height: 150px; }
  .front__brand {
    position: absolute; top: 86px; left: 0; right: 0;
    display: flex; align-items: center; justify-content: center; gap: 18px;
  }
  .brand-dot {
    width: 54px; height: 54px; border-radius: 50%;
    background: var(--sunset); flex: none;
  }
  .brand-name {
    color: var(--sunset); font-weight: 700; font-size: 48px; line-height: 1.05;
  }
  .brand-name span { display: block; font-size: 22px; }
  .front__offer {
    position: absolute; top: 214px; left: 0; right: 0;
    text-align: center;
    color: var(--navy); font-weight: 700; font-size: 22px; line-height: 1.2;
  }
  .front__tagline {
    position: absolute; left: 30px; bottom: 34px;
    color: var(--paper); font-weight: 700; font-size: 20px;
  }

  /* ---------- back ---------- */
  .back__message {
    position: absolute; top: 22px; left: 20px; width: 300px;
    font-size: 10.5px; font-style: italic; line-height: 1.45; text-align: center;
  }
  .back__message p + p { margin-top: 6px; }
  .back__brand-panel {
    position: absolute; top: 128px; left: 0; width: 330px; height: 150px;
    background: var(--panel);
    display: flex; align-items: center; justify-content: center; gap: 12px;
    padding: 0 18px;
  }
  .back__brand-panel .brand-dot { width: 30px; height: 30px; background: var(--paper); }
  .back__brand-panel .brand-name { color: var(--paper); font-size: 27px; }
  .back__brand-panel .brand-name span { font-size: 14px; }
  .back__contact {
    position: absolute; left: 22px; bottom: 20px;
    font-size: 11px; font-style: italic; line-height: 1.5;
  }
  .back__contact .label { padding-left: 10px; text-transform: uppercase; }
  .back__contact .phone {
    display: inline-block; padding-left: 10px;
    font-size: 15px; font-weight: 700; font-style: normal; color: var(--navy);
    line-height: 1.35;
  }
  .back__social {
    position: absolute; left: 240px; bottom: 62px;
    display: flex; gap: 6px;
  }
  .back__social i { width: 20px; height: 20px; border-radius: 50%; display: block; }
  .back__social .s1 { background: var(--sky); }
  .back__social .s2 { background: var(--ocean); }
  .back__social .s3 { background: var(--coral); }
  .back__divider {
    position: absolute; top: 0; bottom: 0; left: 336px; width: 1px; background: #eeeeee;
  }
  .back__stamp {
    position: absolute; top: 20px; right: 26px; width: 82px; height: 84px;
    border: 1px solid var(--rule);
  }
  .back__address-lines {
    position: absolute; left: 366px; right: 26px; top: 150px;
    display: flex; flex-direction: column; gap: 36px;
  }
  .back__address-lines span { display: block; height: 1px; background: var(--rule); }
</style>
</head>
<body>

  <section class="postcard front" aria-label="Postcard front">
    <div class="front__top-band"></div>
    <p class="front__web">www.sandpiperrentalsgulf.com</p>
    <svg class="front__wave" viewBox="0 0 640 150" preserveAspectRatio="none" aria-hidden="true">
      <path d="M0 48 C 150 80, 330 78, 470 40 C 540 22, 600 10, 640 4 L640 150 L0 150 Z" fill="var(--navy)"/>
    </svg>
    <div class="front__brand">
      <i class="brand-dot"></i>
      <p class="brand-name">Sandpiper<span>Rentals and Management Company</span></p>
    </div>
    <p class="front__offer">New clients this month: enjoy reduced rates!</p>
    <p class="front__tagline">" Relax - We'll take care of it "</p>
  </section>

  <section class="postcard back" aria-label="Postcard back">
    <div class="back__message">
      <p>Not renting your vacation home?<br>Let us help you maintain the value of your investment.</p>
      <p>Management walk-throughs upon each check out.<br>Quarterly and seasonal maintenance checks scheduled.<br>In house maintenance personnel.<br>No charge for light bulb and filter change.</p>
    </div>
    <div class="back__brand-panel">
      <i class="brand-dot"></i>
      <p class="brand-name">Sandpiper<span>Rentals and Management Company</span></p>
    </div>
    <address class="back__contact">
      <span class="label">Call us,</span><br>
      <span class="phone">1-555-014-2287</span><br>
      <span class="phone">+1 (555) 014-3690</span><br>
      www.sandpiperrentalsgulf.com<br>
      sandpiperrentalsgulf@mailbox.com<br>
      PO Box 4410 Gull Harbor, TX 70000
    </address>
    <div class="back__social" aria-hidden="true"><i class="s1"></i><i class="s2"></i><i class="s3"></i></div>
    <div class="back__divider"></div>
    <div class="back__stamp" aria-label="Stamp area"></div>
    <div class="back__address-lines" aria-label="Mailing address">
      <span></span><span></span><span></span><span></span><span></span>
    </div>
  </section>

</body>
</html>
```